Blog Header Design for Programming Site

I am about to setup a blog using Typepad and I would like a custom graphic design to give my website that much needed unique look. The blog (to be called Marcus & Dolph) is largely about programming, especially artificial intelligence. Books reviews might be included from time to time. This is not a business, but a personal website meant to display our programming skill sets.
Updates

We have gotten 2 designs from 2 different designers that we are pretty fond of.  Just in case, I want people to know that it should not be restricted to simply showing our faces.  You could have us with bodies doing something.  As an example, one holding a laptop and the other holding a Varnell's cube or something.  We want our faces somewhere, but it doesn't have to be just faces.

Target Market(s)

Anyone interested in programming or potential employers.

Industry/Entity Type

Software

Requirements
Must have
• Graphic versions of our faces. Included are some JPGs. Marcus 1, Marcus 2 and Marcus 3 is of course Marcus while Wenqiu 1 and Wenqiu 2 are Dolph. They do not have to be super detailed. Not exactly sure what we want in terms of how our faces should be used. It could be easily be "Marcus & Dolph" in the middle with Marcus leaning on the word Marcus doing something and Dolph leaning on the word Dolph doing something. This is totally up to you.
Nice to have
• Even though the subject matter is sort of nerdy, we are probably wanting to go for an edgy look, sort of like something you expect see on blogs that deal with games.
Should not have
• Let your creative juices go. Should simply not have a nerdy look to it. Last time I requested a design, some people submitted some designs using bright colors that made it look really childish.

```html
<!DOCTYPE html>
<html lang="en">
<head>
<meta charset="utf-8">
<title>Marcus &amp; Dolph</title>
<link href="https://fonts.googleapis.com/css2?family=Orbitron:wght@700&display=swap" rel="stylesheet">
<style>
  :root {
    --ink: #0b0b0b;
    --panel-light: #b3a597;
    --panel-mid: #978779;
    --panel-dark: #7b6d61;
    --portrait-light: #bfb4aa;
    --portrait-dark: #3a3632;
    --accent: #f4e600;
    --edge: #e9e4dc;
  }
  html, body {
    margin: 0;
    padding: 0;
    width: 1200px;
    height: 304px;
    overflow: hidden;
    background: var(--ink);
  }
  .header {
    position: relative;
    width: 1200px;
    height: 304px;
    background: var(--ink);
    overflow: hidden;
  }
  .stage {
    position: absolute;
    left: 12px;
    top: 12px;
    width: 1176px;
    height: 280px;
    background: linear-gradient(160deg, var(--panel-light) 0%, var(--panel-mid) 45%, var(--panel-dark) 100%);
  }
  .streak {
    position: absolute;
    left: 300px;
    top: 100px;
    width: 260px;
    height: 40px;
    background: linear-gradient(90deg, rgba(233,228,220,0) 0%, rgba(233,228,220,0.35) 50%, rgba(233,228,220,0) 100%);
    transform: rotate(-28deg);
  }
  .portrait {
    position: absolute;
    top: 12px;
    height: 280px;
  }
  .portrait--marcus {
    left: 12px;
    width: 268px;
    background: radial-gradient(ellipse at 55% 50%, var(--portrait-light) 0%, #8d847b 45%, var(--portrait-dark) 85%, var(--ink) 100%);
  }
  .portrait--dolph {
    right: 12px;
    width: 270px;
    background: radial-gradient(ellipse at 50% 48%, var(--portrait-light) 0%, #8d847b 45%, var(--portrait-dark) 85%, var(--ink) 100%);
  }
  .title {
    position: absolute;
    left: 380px;
    top: 26px;
    width: 460px;
    margin: 0;
    text-align: center;
    font-family: "Orbitron", sans-serif;
    font-weight: 700;
    font-size: 74px;
    line-height: 80px;
    color: var(--accent);
    letter-spacing: 1px;
    text-shadow:
      -3px -3px 0 var(--ink), 3px -3px 0 var(--ink), -3px 3px 0 var(--ink), 3px 3px 0 var(--ink),
      0 -3px 0 var(--ink), 0 3px 0 var(--ink), -3px 0 0 var(--ink), 3px 0 0 var(--ink),
      -5px -5px 0 var(--edge), 5px 5px 0 var(--edge), 5px -5px 0 var(--edge), -5px 5px 0 var(--edge);
  }
  .title span { display: block; }
  .frame {
    position: absolute;
    inset: 0;
  }
</style>
</head>
<body>
<header class="header">
  <div class="stage"><div class="streak"></div></div>
  <div class="portrait portrait--marcus" role="img" aria-label="Halftone portrait of Marcus"></div>
  <div class="portrait portrait--dolph" role="img" aria-label="Halftone portrait of Dolph"></div>
  <h1 class="title"><span>marcus</span><span>and</span><span>dolph</span></h1>
  <svg class="frame" width="1200" height="304" viewBox="0 0 1200 304" aria-hidden="true">
    <g fill="none" stroke="#f4e600" stroke-width="5">
      <polyline points="8,52 8,8 52,8"/>
      <polyline points="1148,8 1192,8 1192,52"/>
      <polyline points="8,252 8,296 52,296"/>
      <polyline points="1148,296 1192,296 1192,252"/>
    </g>
  </svg>
</header>
</body>
</html>
```